We are looking for a 2-page (front and back) 3.67" x 8.5" rack card. . Please refer back to our other Rack Cards for a similar look and feel to the card. This one is titled: Myths and Truths About Memory Loss
The document is for older readers. Do not put text over graphics and keep it simple and easy to read with high contrast.
We want some very simple design element(s) incorporated that convey Native American communities or heritage. But NO headdress, teepee graphics, owls etc. I have included some graphics, please use your creative discretion to use which ones look good on the cards. Please remember to include the funding statement - it can be in a very small font 6/7 point. For more information about our project, please visit https://orvelmesa.net/mind-care/library - This rack card is supported by the Bureau for Wellness Tracking and Outreach (BWT) of the Federal Office of Family and Care Affairs (FOF) as part of a financial assistance award totaling $1,053,119.36 with 100 percent funded by BWT/FOF. The contents are those of the author(s) and do not necessarily represent the official views of, nor an endorsement, by BWT/FOF, or the U.S. Government.
Please feel free to choose one of each of the 2 logos that looks best. We have the QT7 logo and the Mind Wellness Support Hub logo we would like to add. I have added the document and there are images to choose from to use in the rack card. We definitely want to incorporate the coyote in this rack card since it is culturally significant.

```html
<!DOCTYPE html>
<html lang="en">
<head>
<meta charset="utf-8">
<title>Myths and Truths About Memory Loss – Rack Card</title>
<link rel="stylesheet" href="https://fonts.googleapis.com/css2?family=Luckiest+Guy&family=Poppins:ital,wght@0,400;0,600;0,700;1,400&display=swap">
<style>
  :root{
    --backdrop:#545454;
    --paper:#ffffff;
    --teal-deep:#1f5a63;
    --teal:#4ea8b1;
    --red:#b9524d;
    --maroon:#7d2b30;
    --ink:#262626;
    --rule:#a9666a;
    --river:#5c8f6a;
  }
  *{box-sizing:border-box;margin:0;padding:0}
  html,body{width:1141px;height:1200px;overflow:hidden;background:var(--backdrop)}
  body{position:relative;font-family:"Poppins",sans-serif;color:var(--ink)}
  .card{position:absolute;top:105px;width:695px;height:1607px;background:var(--paper);
    transform:scale(.6085);transform-origin:0 0;overflow:hidden}
  .card--front{left:106px}
  .card--back{left:617px}
  .abs{position:absolute}
  .display{font-family:"Luckiest Guy",sans-serif;letter-spacing:1px;font-weight:400}

  /* front header */
  .brand{left:32px;top:40px;width:260px}
  .brand__mark{display:flex;align-items:center;gap:12px;font-weight:700;font-size:64px;color:var(--teal);line-height:1}
  .brand__mark span.dot{width:22px;height:22px;border-radius:50%;background:var(--teal)}
  .brand__name{margin-top:16px;font-weight:700;font-size:15px;line-height:1.25;color:var(--red);text-transform:uppercase}
  .hero-photo{left:0;top:0;width:695px;height:350px}
  .title-band{left:0;top:195px;width:330px;height:160px;background:var(--teal-deep)}
  .title{left:33px;top:205px;color:#fff;font-size:35px;line-height:43px}
  .intro{left:0;top:350px;width:695px;height:187px;background:var(--teal-deep)}
  .intro p{position:absolute;left:35px;top:30px;width:610px;color:#fff;font-size:18.5px;line-height:22px}
  .zigzag{left:0;top:537px;width:695px;height:26px;background:linear-gradient(90deg,#c98a87,#8fc3c8,#c98a87)}

  /* myth vs truth */
  .mvt{left:0;width:695px}
  .mvt svg{display:block}
  .row-text{font-size:18px;line-height:22px;color:var(--ink)}
  .myth{left:103px;width:225px}
  .truth{left:373px;width:250px}

  .gallery{left:28px;top:1090px;width:640px;height:322px;border:14px solid #9ccbd0;background:#fff}
  .gallery__photo{position:absolute;height:122px}

  .footer{left:0;top:1443px;width:695px;height:164px;background:var(--teal-deep);color:#fff}
  .footer__pattern{position:absolute;left:0;bottom:0;width:695px;height:50px;background:linear-gradient(180deg,var(--teal-deep),#3f8f98)}
  .quote{left:45px;top:28px;width:310px;font-size:15.5px;line-height:24px;border-right:1px solid #9cc;border-bottom:1px solid #9cc;padding-bottom:6px}
  .quote__mark{position:absolute;font-family:"Poppins",sans-serif;font-weight:700;font-size:30px}
  .attribution{right:38px;top:30px;text-align:right;font-size:17px;line-height:25px}
  .attribution b{font-weight:700}
  .attribution i{font-style:italic}

  /* back */
  .do-photo{left:300px;top:647px;width:395px;height:328px}
  .do-hex{left:18px;top:647px;width:380px;height:328px}
  .do-text{left:75px;top:690px;width:270px;text-align:center;color:#fff}
  .do-text h2{font-size:29px;margin-bottom:14px}
  .do-text p{font-size:17.5px;line-height:22px}
  .more{left:35px;top:1015px;width:625px;height:48px}
  .more h2{position:absolute;left:0;top:10px;width:625px;text-align:center;color:#fff;font-size:26px}
  .links-frame{left:30px;top:1100px;width:635px;height:300px;border:14px solid #cfe6e8;border-left-color:#e8c9c7;border-right-color:#e8c9c7}
  .links{left:60px;top:1140px;width:580px;list-style:none}
  .links li{position:relative;padding-left:16px;margin-bottom:18px;font-size:17px;line-height:24px}
  .links li::before{content:"";position:absolute;left:0;top:10px;width:6px;height:6px;border-radius:50%;background:var(--ink)}
  .links a{color:var(--maroon);text-decoration:none;display:block;margin-top:4px}
  .funding{left:0;top:38px;width:695px;text-align:center;font-weight:700;font-size:17px}
</style>
</head>
<body>

<!-- FRONT -->
<section class="card card--front">
  <div class="abs hero-photo" role="img" aria-label="Photo of a river winding through a forested canyon"
       style="background:linear-gradient(180deg,#7fb8e0 0%,#4c7f52 35%,#3d6b46 70%,#5f8d9a 100%);clip-path:polygon(395px 0,695px 0,695px 350px,300px 350px)"></div>
  <div class="abs title-band"></div>
  <div class="abs brand">
    <div class="brand__mark"><span class="dot"></span>QT7</div>
    <div class="brand__name">Quill Trail Council<br>for Native Elders</div>
  </div>
  <h1 class="abs title display">Myths and<br>Truths about<br>Memory Loss</h1>
  <div class="abs intro">
    <p>People sometimes believe things about memory loss that are not true. Misunderstandings can make it harder for Elders in Native communities to get the help they need when they start having memory issues. Below are some common myths and truths about memory loss, Alzheimer's disease, and related dementias</p>
  </div>
  <div class="abs zigzag" role="img" aria-label="Decorative zigzag pattern band"></div>

  <div class="abs mvt" style="top:580px">
    <svg width="695" height="480" viewBox="0 0 695 480">
      <polygon points="32,77 75,52 320,52 320,102 75,102" fill="var(--teal-deep)"/>
      <polygon points="374,52 620,52 665,77 620,102 374,102" fill="var(--teal)"/>
      <text x="175" y="88" text-anchor="middle" font-family="Luckiest Guy" font-size="28" fill="#fff" letter-spacing="1">MYTH</text>
      <text x="527" y="88" text-anchor="middle" font-family="Luckiest Guy" font-size="28" fill="#fff" letter-spacing="1">TRUTH</text>
      <path d="M347 5 L339 22 L355 22 Z" fill="var(--maroon)"/>
      <line x1="347" y1="20" x2="347" y2="50" stroke="var(--maroon)" stroke-width="2"/>
      <circle cx="347" cy="77" r="27" fill="#fff" stroke="var(--maroon)" stroke-width="3"/>
      <text x="347" y="87" text-anchor="middle" font-family="Luckiest Guy" font-size="26" fill="var(--teal)">VS</text>
      <path d="M378 77 H400 M400 70 L418 77 L400 84 Z" stroke="var(--maroon)" stroke-width="2" fill="var(--maroon)"/>
      <path d="M276 70 l8 7 -8 7 M286 70 l8 7 -8 7 M296 70 l8 7 -8 7" stroke="var(--red)" stroke-width="2" fill="none"/>
      <line x1="347" y1="105" x2="347" y2="477" stroke="var(--rule)" stroke-width="1.5"/>
      <g stroke="var(--rule)" stroke-width="1.5" fill="var(--maroon)">
        <line x1="60" y1="175" x2="640" y2="175"/><path d="M50 175 l22 -7 -6 7 6 7z"/><path d="M650 175 l-22 -7 6 7 -6 7z"/>
        <line x1="60" y1="337" x2="640" y2="337"/><path d="M50 337 l22 -7 -6 7 6 7z"/><path d="M650 337 l-22 -7 6 7 -6 7z"/>
        <line x1="60" y1="477" x2="640" y2="477"/><path d="M50 477 l22 -7 -6 7 6 7z"/><path d="M650 477 l-22 -7 6 7 -6 7z"/>
      </g>
    </svg>
  </div>
  <p class="abs row-text myth" style="top:697px">Getting Alzheimer's is a normal part of aging.</p>
  <p class="abs row-text truth" style="top:697px">It is a disease that not everyone will get.</p>
  <p class="abs row-text myth" style="top:765px">Memory problems and forgetfulness are definite signs of dementia.</p>
  <p class="abs row-text truth" style="top:765px">Memory problems do not solely determine if they are dementia. Other medical conditions can cause memory problems. Talk to your doctor.</p>
  <p class="abs row-text myth" style="top:928px">Only older people can get Alzheimer's disease.</p>
  <p class="abs row-text truth" style="top:928px">There have been cases for people as young as twenty-five, though it is rare to undergo treatment.</p>

  <div class="abs gallery" role="img" aria-label="Framed collage of six photos: dancers in regalia, a canyon river bend, an Elder seated, colorful corn, Elders gathered in a circle, and a grandmother with children">
    <div class="gallery__photo" style="left:16px;top:16px;width:190px;background:#8a3b34"></div>
    <div class="gallery__photo" style="left:212px;top:16px;width:186px;background:linear-gradient(#e3a56b,#4a8a9c)"></div>
    <div class="gallery__photo" style="left:404px;top:16px;width:205px;background:#6d6863"></div>
    <div class="gallery__photo" style="left:16px;top:144px;width:190px;background:#9a5a3a"></div>
    <div class="gallery__photo" style="left:212px;top:144px;width:186px;background:#a88468"></div>
    <div class="gallery__photo" style="left:404px;top:144px;width:205px;background:#5d5552"></div>
  </div>

  <footer class="abs footer">
    <blockquote class="abs quote">
      <span class="quote__mark" style="left:-25px;top:-12px">“</span>
      The beauty in life is each day is a new day to try again and be a better version of myself than yesterday.
      <span class="quote__mark" style="right:-30px;bottom:-12px">”</span>
    </blockquote>
    <p class="abs attribution"><b>—Lena Tallgrass (Blackfeet).</b><br><i>personal communication<br>with the author.</i></p>
    <div class="footer__pattern" role="img" aria-label="Decorative zigzag pattern strip"></div>
  </footer>
</section>

<!-- BACK -->
<section class="card card--back">
  <div class="abs mvt" style="top:28px">
    <svg width="695" height="590" viewBox="0 0 695 590">
      <polygon points="32,77 75,52 320,52 320,102 75,102" fill="var(--teal-deep)"/>
      <polygon points="374,52 620,52 665,77 620,102 374,102" fill="var(--teal)"/>
      <text x="175" y="88" text-anchor="middle" font-family="Luckiest Guy" font-size="28" fill="#fff" letter-spacing="1">MYTH</text>
      <text x="527" y="88" text-anchor="middle" font-family="Luckiest Guy" font-size="28" fill="#fff" letter-spacing="1">TRUTH</text>
      <path d="M347 5 L339 22 L355 22 Z" fill="var(--maroon)"/>
      <line x1="347" y1="20" x2="347" y2="50" stroke="var(--maroon)" stroke-width="2"/>
      <circle cx="347" cy="77" r="27" fill="#fff" stroke="var(--maroon)" stroke-width="3"/>
      <text x="347" y="87" text-anchor="middle" font-family="Luckiest Guy" font-size="26" fill="var(--teal)">VS</text>
      <path d="M378 77 H400 M400 70 L418 77 L400 84 Z" stroke="var(--maroon)" stroke-width="2" fill="var(--maroon)"/>
      <path d="M276 70 l8 7 -8 7 M286 70 l8 7 -8 7 M296 70 l8 7 -8 7" stroke="var(--red)" stroke-width="2" fill="none"/>
      <line x1="347" y1="105" x2="347" y2="582" stroke="var(--rule)" stroke-width="1.5"/>
      <g stroke="var(--rule)" stroke-width="1.5" fill="var(--maroon)">
        <line x1="60" y1="242" x2="640" y2="242"/><path d="M50 242 l22 -7 -6 7 6 7z"/><path d="M650 242 l-22 -7 6 7 -6 7z"/>
        <line x1="60" y1="424" x2="640" y2="424"/><path d="M50 424 l22 -7 -6 7 6 7z"/><path d="M650 424 l-22 -7 6 7 -6 7z"/>
        <line x1="60" y1="582" x2="640" y2="582"/><path d="M50 582 l22 -7 -6 7 6 7z"/><path d="M650 582 l-22 -7 6 7 -6 7z"/>
      </g>
    </svg>
  </div>
  <p class="abs row-text myth" style="top:145px">People with Alzheimer's disease cannot be happy.</p>
  <p class="abs row-text truth" style="top:145px">A person with memory loss can experience strong moods and emotions but still enjoy life and relationships.</p>
  <p class="abs row-text myth" style="top:283px">Dementia can be prevented by a certain supplement or food.</p>
  <p class="abs row-text truth" style="top:283px">Healthy eating may help overall wellness, including brain health. No additional supplements will completely prevent the onset of dementia.</p>
  <p class="abs row-text myth" style="top:465px">Alzheimer's is reversible through prescription drugs.</p>
  <p class="abs row-text truth" style="top:465px">There are prescription drugs to address symptoms of Alzheimer's and dementia, but there are no medicines that can reverse them.</p>

  <div class="abs do-photo" role="img" aria-label="Photo of a ribbon skirt with rainbow ribbons and a beaded heart"
       style="background:linear-gradient(90deg,#6fbf6a,#e0457a 30%,#4a7fd0 55%,#d9c7a8 80%,#efe8dc)"></div>
  <svg class="abs do-hex" viewBox="0 0 380 328" width="380" height="328" aria-hidden="true">
    <polygon points="95,0 285,0 380,164 285,328 95,328 0,164" fill="var(--teal-deep)"/>
  </svg>
  <div class="abs do-text">
    <h2 class="display">What you can do</h2>
    <p>If you or someone you love is having memory problems, do not wait. Talk to a healthy provider you trust. Learning the truth can help keep our Elders strong and supported.</p>
  </div>

  <div class="abs more">
    <svg width="625" height="48" viewBox="0 0 625 48" aria-hidden="true"><polygon points="0,24 24,0 601,0 625,24 601,48 24,48" fill="var(--teal-deep)"/></svg>
    <h2 class="display">For more myth-busting information</h2>
  </div>
  <div class="abs links-frame" role="img" aria-label="Decorative border of teal and red feathers"></div>
  <ul class="abs links">
    <li>12 Common Alzheimer's Disease Myths on Kinhaven.com:<a href="#">https://www.kinhaven.com/c/memory-myths-busted/</a></li>
    <li>Memory Alliance Network Myths vs. Facts:<a href="#">https://www.memoryalliance.org/research-and-progress/clinical-trials/myths-vs-facts</a></li>
    <li>QT7 Brain Health Resources:<a href="#">https://orvelmesa.net/library/</a></li>
  </ul>

  <footer class="abs footer">
    <p class="abs funding">Orvelmesa.net (Funding Statement)</p>
    <svg class="abs" style="left:105px;top:70px" width="490" height="24" viewBox="0 0 490 24" aria-hidden="true">
      <path d="M2 5 l9 7 -9 7 M12 5 l9 7 -9 7 M22 5 l9 7 -9 7" stroke="#fff" stroke-width="2" fill="none"/>
      <line x1="30" y1="12" x2="470" y2="12" stroke="#fff" stroke-width="2"/>
      <path d="M468 4 L488 12 L468 20 Z" fill="#fff"/>
    </svg>
    <div class="footer__pattern" role="img" aria-label="Decorative zigzag pattern strip"></div>
  </footer>
</section>

</body>
</html>
```